Quillfern Nightclub Flyer (Updated)

Flyer for facebook, square is fine, or rectangular. Here is the text:
QUILLFERN
Nightclub + Lounge
presents

SPLIT DECK WEDNESDAY
Nov 29 2018

CLUB FLOOR:
GORDY B2B RALPH
THEODORE BRUSKVIK

LOUNGE:
OTIS B2B HALF TIDE
COPPER FENWICK

Powered by HALVERN Acoustics
4716 Larchmere Avenue 21+ 9pm-2am
quillfernvenue-example.com for VIP booth inquiries

Target Market(s)

Nightclub

Industry/Entity Type

Night Club

Font styles to use
Sans Serif

Colors

Designer to choose colors to be used in the design.

Requirements
Must have
• All the text listed, and plz keep the theme of the attached files. We want to stay consistent with the Quillfern brand
Nice to have
• Try to stay with the theme from the attachments
Should not have
• Dont' stray to far from the general theme we have from the attachments

```html
<!DOCTYPE html>
<html lang="en">
<head>
<meta charset="utf-8">
<title>Quillfern Nightclub – Split Deck Wednesday Flyers</title>
<link rel="stylesheet" href="https://fonts.googleapis.com/css2?family=Bodoni+Moda:wght@600&family=Montserrat:wght@500;600;700&display=swap">
<style>
  :root {
    --stage: #3a4a63;
    --gold-dark: #97764a;
    --gold-mid: #c9a878;
    --gold-light: #e2c89e;
    --gold-text: #a8895c;
    --gold-gradient: linear-gradient(90deg, var(--gold-dark), var(--gold-light) 50%, var(--gold-dark));
    --ink-dark: #000000;
    --ink-light: #ffffff;
    --paper: #ffffff;
    --text-on-paper: #3a3a3a;
    --muted-on-paper: #9a9ca1;
    --serif: "Bodoni Moda", "Didot", serif;
    --sans: "Montserrat", "Helvetica Neue", sans-serif;
  }

  * { margin: 0; padding: 0; box-sizing: border-box; }

  html, body {
    width: 1200px;
    height: 640px;
    overflow: hidden;
    background: var(--stage);
  }

  .stage {
    position: relative;
    width: 1200px;
    height: 640px;
  }

  .flyer {
    position: absolute;
    top: 61px;
    width: 518px;
    height: 517px;
    text-align: center;
    font-family: var(--sans);
  }
  .flyer--dark  { left: 78px;  background: var(--ink-dark); color: var(--ink-light); }
  .flyer--light { left: 618px; background: var(--paper);    color: var(--text-on-paper); }

  .frame {
    position: absolute;
    border-style: solid;
    border-image: var(--gold-gradient) 1;
  }
  .frame--outer { inset: 21px; border-width: 6px; }
  .frame--inner { inset: 38px; border-width: 3px; }

  .line {
    position: absolute;
    left: 0;
    right: 0;
    transform: translateY(-50%);
    white-space: nowrap;
  }

  .brand {
    top: 104px;
    font-family: var(--sans);
    font-weight: 600;
    font-size: 32px;
    letter-spacing: 3px;
    line-height: 1;
  }

  .brand-tagline {
    top: 129px;
    font-size: 7.5px;
    letter-spacing: 1.6px;
    font-weight: 500;
  }
  .flyer--light .brand-tagline { color: var(--muted-on-paper); }

  .presents {
    top: 154px;
    font-size: 9px;
    letter-spacing: 1.4px;
    font-weight: 500;
  }

  .rule {
    position: absolute;
    left: 103px;
    width: 312px;
    height: 3px;
    background: linear-gradient(90deg, transparent, var(--gold-mid) 25%, var(--gold-light) 50%, var(--gold-mid) 75%, transparent);
  }
  .rule--top    { top: 176px; }
  .rule--bottom { top: 253px; }

  .headline {
    top: 207px;
    font-family: var(--serif);
    font-weight: 600;
    font-size: 29px;
    color: var(--gold-text);
    letter-spacing: 0.3px;
  }

  .event-date {
    top: 237px;
    font-size: 12.5px;
    font-weight: 600;
    letter-spacing: 3.4px;
  }

  .floor-label {
    position: absolute;
    left: 50%;
    transform: translateX(-50%);
    width: 116px;
    height: 16px;
    line-height: 16px;
    background: linear-gradient(90deg, var(--gold-dark), var(--gold-mid));
    color: var(--ink-light);
    font-size: 9.5px;
    font-weight: 600;
    letter-spacing: 2px;
  }
  .floor-label--club   { top: 282px; }
  .floor-label--lounge { top: 341px; }

  .act {
    font-size: 10px;
    font-weight: 700;
    letter-spacing: 1.6px;
  }
  .act--club-1   { top: 308px; }
  .act--club-2   { top: 321px; }
  .act--lounge-1 { top: 367px; }
  .act--lounge-2 { top: 380px; }

  .fine-print {
    font-size: 6.5px;
    font-weight: 500;
    letter-spacing: 1px;
  }
  .fine-print--sound   { top: 412px; }
  .fine-print--venue   { top: 422px; }
  .fine-print--booking { top: 432px; font-weight: 700; }
</style>
</head>
<body>
<main class="stage">

  <article class="flyer flyer--dark">
    <div class="frame frame--outer"></div>
    <div class="frame frame--inner"></div>
    <h1 class="line brand">QUILLFERN</h1>
    <p class="line brand-tagline">NIGHTCLUB + LOUNGE</p>
    <p class="line presents">PRESENTS</p>
    <div class="rule rule--top"></div>
    <h2 class="line headline">SPLIT DECK WEDNESDAY</h2>
    <p class="line event-date">NOVEMBER 29, 2018</p>
    <div class="rule rule--bottom"></div>
    <p class="floor-label floor-label--club">CLUB FLOOR:</p>
    <p class="line act act--club-1">GORDY B2B RALPH</p>
    <p class="line act act--club-2">THEODORE BRUSKVIK</p>
    <p class="floor-label floor-label--lounge">LOUNGE:</p>
    <p class="line act act--lounge-1">OTIS B2B HALF TIDE</p>
    <p class="line act act--lounge-2">COPPER FENWICK</p>
    <p class="line fine-print fine-print--sound">POWERED BY HALVERN ACOUSTICS</p>
    <p class="line fine-print fine-print--venue">4716 LARCHMERE AVENUE 21+ 9PM-2AM</p>
    <p class="line fine-print fine-print--booking">QUILLFERNVENUE-EXAMPLE.COM FOR VIP BOOTH INQUIRIES</p>
  </article>

  <article class="flyer flyer--light">
    <div class="frame frame--outer"></div>
    <div class="frame frame--inner"></div>
    <h1 class="line brand">QUILLFERN</h1>
    <p class="line brand-tagline">NIGHTCLUB + LOUNGE</p>
    <p class="line presents">PRESENTS</p>
    <div class="rule rule--top"></div>
    <h2 class="line headline">SPLIT DECK WEDNESDAY</h2>
    <p class="line event-date">NOVEMBER 29, 2018</p>
    <div class="rule rule--bottom"></div>
    <p class="floor-label floor-label--club">CLUB FLOOR:</p>
    <p class="line act act--club-1">GORDY B2B RALPH</p>
    <p class="line act act--club-2">THEODORE BRUSKVIK</p>
    <p class="floor-label floor-label--lounge">LOUNGE:</p>
    <p class="line act act--lounge-1">OTIS B2B HALF TIDE</p>
    <p class="line act act--lounge-2">COPPER FENWICK</p>
    <p class="line fine-print fine-print--sound">POWERED BY HALVERN ACOUSTICS</p>
    <p class="line fine-print fine-print--venue">4716 LARCHMERE AVENUE 21+ 9PM-2AM</p>
    <p class="line fine-print fine-print--booking">QUILLFERNVENUE-EXAMPLE.COM FOR VIP BOOTH INQUIRIES</p>
  </article>

</main>
</body>
</html>
```